New Business Card Design Project

Need a design that will create an impact / strong impression towards our clients for our business. We are in the lighting business and we do lighting retrofits for large commercial to industrial clientele.

Target Market(s)

Lighting Industry

Industry/Entity Type

Business

Other font styles liked:
• we would like to use the font on our logo, not sure what it is though..

Requirements
Must have
• Our logo.
Nice to have
• We are open to suggestions that have to do with lighting.

```html
<!DOCTYPE html>
<html lang="en">
<head>
<meta charset="utf-8">
<title>Brightway Retrofit Group – Business Card</title>
<link href="https://fonts.googleapis.com/css2?family=Montserrat:wght@600;800&family=Lato:wght@400;700&display=swap" rel="stylesheet">
<style>
  :root {
    --backdrop: #1e1e1e;
    --green-deep: #0f3d1a;
    --green-dark: #1d4a27;
    --green-brand: #108544;
    --green-light: #6cc05a;
    --white: #ffffff;
    --ink-grey: #666666;
  }
  * { margin: 0; padding: 0; box-sizing: border-box; }
  html, body { width: 1200px; height: 897px; overflow: hidden; background: var(--backdrop); }
  .canvas { position: relative; width: 1200px; height: 897px; }

  .card { position: absolute; left: 314px; width: 557px; overflow: hidden; }

  /* Front */
  .card-front {
    top: 120px; height: 318px;
    background: radial-gradient(ellipse at 85% 10%, #2f4b2e 0%, #1a4a23 40%, var(--green-deep) 100%);
    color: var(--white);
    font-family: "Montserrat", sans-serif;
  }
  .front-brand {
    position: absolute; left: 0; right: 0; top: 118px; text-align: center;
  }
  .front-brand .wordmark {
    display: inline-flex; align-items: center; gap: 12px;
    font-weight: 800; font-size: 40px; letter-spacing: 2px; color: var(--white);
  }
  .wordmark .mark-square { width: 22px; height: 22px; background: var(--green-light); }
  .front-brand .rule { width: 296px; height: 2px; background: var(--green-light); margin: 8px auto 6px; }
  .front-brand .company { font-weight: 600; font-size: 11.5px; letter-spacing: 1.2px; }
  .front-web {
    position: absolute; left: 0; right: 0; top: 282px; text-align: center;
    font-family: "Lato", sans-serif; font-size: 12px; letter-spacing: 1.5px;
  }
  .front-web .accent { color: var(--green-light); }

  /* Back */
  .card-back { top: 470px; height: 316px; background: var(--white); font-family: "Lato", sans-serif; }
  .side-strip { position: absolute; left: 0; top: 0; width: 27px; height: 100%; background: var(--green-brand); }
  .side-strip .highlight { position: absolute; left: 0; top: 147px; width: 27px; height: 48px; background: var(--green-light); border-top: 2px solid var(--white); border-bottom: 2px solid var(--white); }

  .back-brand { position: absolute; left: 48px; top: 40px; font-family: "Montserrat", sans-serif; }
  .back-brand .wordmark {
    display: flex; align-items: center; gap: 9px;
    font-weight: 800; font-size: 30px; letter-spacing: 1.5px; color: var(--green-dark);
  }
  .back-brand .wordmark .mark-square { width: 16px; height: 16px; background: var(--green-brand); }
  .back-brand .rule { width: 216px; height: 1.5px; background: var(--green-brand); margin: 4px 0 3px; }
  .back-brand .company { font-weight: 600; font-size: 8.6px; letter-spacing: 0.6px; color: var(--green-dark); }

  .holder { position: absolute; left: 48px; top: 154px; }
  .holder .name { font-size: 19px; color: var(--green-brand); letter-spacing: 0.3px; }
  .holder .role { font-size: 15px; color: var(--ink-grey); margin-top: -2px; }

  .contacts { position: absolute; left: 52px; top: 221px; list-style: none; }
  .contacts li { display: flex; align-items: center; gap: 10px; height: 17.5px; font-size: 12.5px; color: var(--ink-grey); letter-spacing: 0.4px; }
  .contacts svg { width: 11px; height: 11px; fill: var(--green-brand); }
  .divider { position: absolute; left: 236px; top: 228px; width: 1px; height: 42px; background: #9a9a9a; }
  .address { position: absolute; left: 259px; top: 222px; font-size: 12.5px; line-height: 17.5px; color: var(--ink-grey); letter-spacing: 0.5px; }
  .swoosh { position: absolute; left: 0; bottom: 0; width: 557px; height: 316px; }
</style>
</head>
<body>
<div class="canvas">

  <section class="card card-front">
    <div class="front-brand">
      <div class="wordmark">BRIGHTWAY<span class="mark-square"></span></div>
      <div class="rule"></div>
      <div class="company">BRIGHTWAY RETROFIT GROUP, LLC.</div>
    </div>
    <div class="front-web">www.<span class="accent">brightwayllc</span>.com</div>
  </section>

  <section class="card card-back">
    <div class="side-strip"><div class="highlight"></div></div>

    <svg class="swoosh" viewBox="0 0 557 316" aria-hidden="true">
      <path d="M210 316 C 390 300, 500 270, 557 206 L557 316 Z" fill="#6cc05a"/>
      <path d="M230 316 C 400 302, 505 276, 557 214 L557 316 Z" fill="#ffffff"/>
      <path d="M250 316 C 410 304, 510 282, 557 220 L557 316 Z" fill="#108544"/>
    </svg>

    <div class="back-brand">
      <div class="wordmark">BRIGHTWAY<span class="mark-square"></span></div>
      <div class="rule"></div>
      <div class="company">BRIGHTWAY RETROFIT GROUP, LLC.</div>
    </div>

    <div class="holder">
      <div class="name">DANIEL REYES</div>
      <div class="role">Founder</div>
    </div>

    <ul class="contacts">
      <li><svg viewBox="0 0 24 24"><path d="M6.6 10.8a15 15 0 0 0 6.6 6.6l2.2-2.2c.3-.3.7-.4 1-.2 1.1.4 2.3.6 3.6.6.6 0 1 .4 1 1V20c0 .6-.4 1-1 1A17 17 0 0 1 3 4c0-.6.4-1 1-1h3.5c.6 0 1 .4 1 1 0 1.3.2 2.5.6 3.6.1.3 0 .7-.2 1z"/></svg>0400 527 318</li>
      <li><svg viewBox="0 0 24 24"><path d="M2 5h20v14H2z M2 5l10 8 10-8" /><path d="M3 6l9 7 9-7v-1H3z" fill="#fff"/></svg>hello@brightwayllc.com</li>
      <li><svg viewBox="0 0 24 24"><circle cx="12" cy="12" r="10"/><path d="M2 12h20M12 2c3 3 3 17 0 20M12 2c-3 3-3 17 0 20" stroke="#fff" stroke-width="1.5" fill="none"/></svg>www.brightwayllc.com</li>
    </ul>
    <div class="divider"></div>
    <div class="address">4820 East<br>Canyon Road, Suite<br>C204 Mesa 85201</div>
  </section>

</div>
</body>
</html>
```